Etiketten für Charity Bier gesucht
Zielgruppe
Wir engagieren uns ehrenamtlich für Kinder in Afrika.
In Einsatz-Teams von freiwilligen Helfern, sammeln wir während 8 Monaten Spendengelder, um Kindern in Townships's Südafrikas eine Zukunft zu bauen, in dem wir nicht staatliche Kindertagesstätten engagierter einheimischer Frauen umbauen.
Vorher bestehen die KITA's nur aus rostigen Wellblechhütten, welche nicht isoliert sind und auf dem KITA Gelände befindet sich weder Rasen, noch ein Spielplatz.
Aufgabenstellung
Um Spenden zu sammeln, möchten wir ein Charity Bier auf den Markt bringen.
Infos zu den Maßen der Etiketten: Sie sollten nicht breiter als 8 cm sein. Wichtig ist, dass sich in der Ecke links oben keine Angaben befinden, da die obere linke Kante schräg nach oben verlaufen wird. Welche Angaben müssen zwingend auf den Etiketten zu finden sein?
Die Promill-Angaben (5.2% VOL)
Inhalts-Angabe (33cl) das Logo des Bierherstellers sollte auch mit auf die Etikette (nicht all zu gross) (siehe Bild Nr.2)
Die Info's zum Bier (Biersorte: Tannfelsbräu ORIGINAL)
Der Name des Bier's sollte Charity Bier sein.
Wir möchten auf der Etikette auch folgendes unbedingt vermerken:
'Diese Flache (Bier) füllt 10 Breischalen für Kinder in Afrika'
Ansonsten haben wir überhaupt keine Vorstellung, was wir wörtlich noch auf die Etikette packen möchten (vielleicht fällt euch ja noch was tolles ein:-)
Was wir uns vom Design her so vorstellen:
Ich habe noch 3 Bilder (siehe Bild 3-4) dazugefügt, mit Designs, welche mir auf Anhieb sehr sehr gut gefallen (damit ihr einen Anhaltspunkt habt:-) Aber ich lasse mich auch gerne von anderen Design-Formen überraschen.

```html
<!DOCTYPE html>
<html lang="de">
<head>
<meta charset="utf-8">
<title>Charity Bier – Etiketten</title>
<link rel="stylesheet" href="https://fonts.googleapis.com/css2?family=Rubik+Dirt&family=Oswald:wght@400;500;600&family=Open+Sans:wght@400&display=swap">
<style>
  :root {
    --paper: #ffffff;
    --sun: #f1b400;
    --plum: #951f62;
    --cocoa: #3b2b2f;
    --chili: #e1251b;
    --logo-amber: #d98a1c;
    --logo-gold: #f2b600;
    --blush: #f4c9da;
    --blush-soft: #ead6df;
  }
  html, body {
    margin: 0;
    width: 1200px;
    height: 647px;
    overflow: hidden;
    background: var(--paper);
  }
  .stage {
    position: absolute;
    left: 0; top: 0;
    width: 1040px;
    height: 560px;
    transform: scale(1.1538);
    transform-origin: 0 0;
  }
  .label-wrap {
    position: absolute;
    top: 62px;
    width: 453px;
    height: 451px;
    filter: drop-shadow(4px 5px 5px rgba(0,0,0,0.45));
  }
  .label-wrap--sun  { left: 47px; }
  .label-wrap--plum { left: 545px; }
  .label {
    position: absolute;
    inset: 0;
    overflow: hidden;
  }
  .label--sun  { background: var(--sun);  clip-path: polygon(0 83px, 100% 0, 100% 100%, 0 100%); }
  .label--plum { background: var(--plum); clip-path: polygon(0 90px, 100% 0, 100% 100%, 0 100%); }
  .label__band {
    position: absolute;
    inset: 0;
    background: var(--cocoa);
  }
  .label--sun  .label__band { clip-path: polygon(0 423px, 100% 363px, 100% 100%, 0 100%); }
  .label--plum .label__band { clip-path: polygon(0 428px, 100% 363px, 100% 100%, 0 100%); }

  .brand {
    position: absolute;
    top: 50px;
    left: 0; right: 0;
    text-align: center;
    font: 600 17px/1 "Oswald", sans-serif;
    letter-spacing: 0.3px;
  }
  .label--sun  .brand { color: var(--logo-amber); }
  .label--plum .brand { color: var(--logo-gold); }

  .title {
    position: absolute;
    left: -4px;
    margin: 0;
    font-family: "Rubik Dirt", sans-serif;
    font-weight: 400;
    line-height: 1;
    white-space: nowrap;
  }
  .title--charity { top: 94px; font-size: 106px; letter-spacing: -6px; transform: scaleX(0.93); transform-origin: left; }
  .title--bier    { top: 186px; font-size: 106px; letter-spacing: -4px; color: var(--cocoa); transform: scaleX(0.86); transform-origin: left; }
  .label--sun  .title--charity { color: var(--chili); }
  .label--plum .title--charity { color: var(--paper); }

  .pledge {
    position: absolute;
    left: 243px;
    top: 203px;
    margin: 0;
    font-family: "Oswald", sans-serif;
    font-weight: 500;
  }
  .pledge span { display: block; white-space: nowrap; }
  .pledge__lead   { font-size: 23px; line-height: 27px; }
  .pledge__amount { font-size: 18px; line-height: 24px; }
  .pledge__goal   { font-size: 23px; line-height: 28px; }
  .label--sun  .pledge__lead   { color: var(--chili); }
  .label--sun  .pledge__amount { color: var(--cocoa); }
  .label--sun  .pledge__goal   { color: var(--paper); }
  .label--plum .pledge__lead   { color: var(--cocoa); }
  .label--plum .pledge__amount { color: var(--paper); }
  .label--plum .pledge__goal   { color: var(--blush-soft); }

  .story {
    position: absolute;
    left: 11px;
    top: 307px;
    width: 227px;
    margin: 0;
    font: 400 11.6px/16.5px "Oswald", sans-serif;
    text-align: justify;
    letter-spacing: 0.2px;
  }
  .label--sun  .story { color: var(--paper); }
  .label--plum .story { color: var(--blush); }

  .illustration {
    position: absolute;
    left: 278px;
    top: 302px;
    width: 140px;
    height: 100px;
    border-radius: 40px 40px 60px 60px;
  }
  .label--sun  .illustration { background: radial-gradient(circle at 50% 60%, #c9791a 0%, rgba(201,121,26,0.35) 60%, rgba(241,180,0,0) 75%); }
  .label--plum .illustration { background: radial-gradient(circle at 50% 60%, #f3d4e0 0%, rgba(243,212,224,0.35) 60%, rgba(149,31,98,0) 75%); }

  .variety {
    position: absolute;
    left: 188px;
    top: 421px;
    font: 400 20px/1 "Open Sans", sans-serif;
    letter-spacing: 0.5px;
  }
  .label--sun  .variety { color: var(--paper); }
  .label--plum .variety { color: var(--blush-soft); }

  .facts {
    position: absolute;
    right: 14px;
    top: 400px;
    margin: 0;
    text-align: right;
    font-family: "Oswald", sans-serif;
    font-weight: 400;
  }
  .label--sun  .facts { color: var(--paper); }
  .label--plum .facts { color: var(--blush-soft); }
  .facts__volume { display: block; font-size: 22px; line-height: 24px; }
  .facts__abv    { display: block; font-size: 22px; line-height: 26px; }
  .facts small   { font-size: 12px; }
</style>
</head>
<body>
<main class="stage">

  <article class="label-wrap label-wrap--sun">
    <div class="label label--sun">
      <div class="label__band"></div>
      <div class="brand">Tannfelsbräu</div>
      <h1 class="title title--charity">CHARITY</h1>
      <h2 class="title title--bier">BIER</h2>
      <p class="pledge">
        <span class="pledge__lead">Diese Flasche Bier</span>
        <span class="pledge__amount">füllt 10 KORA Breischalen</span>
        <span class="pledge__goal">für Kinder in Afrika</span>
      </p>
      <p class="story">Das Rezept hat sich im Verlauf der mehrjährigen Geschichte stets weiterentwickelt zu diesem mittlerweile unverkenbar feinen Geschmack. Aus verschiedenen Malzsorten, feinstem Schweizer Hopfen und Tannfels-Wasser</p>
      <div class="illustration" role="img" aria-label="Zeichnung eines Kindes mit einer Schale Brei"></div>
      <div class="variety">ORIGINAL</div>
      <p class="facts">
        <span class="facts__volume">33<small>cl</small></span>
        <span class="facts__abv">5.2 <small>% VOL</small></span>
      </p>
    </div>
  </article>

  <article class="label-wrap label-wrap--plum">
    <div class="label label--plum">
      <div class="label__band"></div>
      <div class="brand">Tannfelsbräu</div>
      <h1 class="title title--charity">CHARITY</h1>
      <h2 class="title title--bier">BIER</h2>
      <p class="pledge">
        <span class="pledge__lead">Diese Flasche Bier</span>
        <span class="pledge__amount">füllt 10 KORA Breischalen</span>
        <span class="pledge__goal">für Kinder in Afrika</span>
      </p>
      <p class="story">Das Rezept hat sich im Verlauf der mehrjährigen Geschichte stets weiterentwickelt zu diesem mittlerweile unverkenbar feinen Geschmack. Aus verschiedenen Malzsorten, feinstem Schweizer Hopfen und Tannfels-Wasser</p>
      <div class="illustration" role="img" aria-label="Zeichnung eines Kindes mit einer Schale Brei"></div>
      <div class="variety">ORIGINAL</div>
      <p class="facts">
        <span class="facts__volume">33<small>cl</small></span>
        <span class="facts__abv">5.2 <small>% VOL</small></span>
      </p>
    </div>
  </article>

</main>
</body>
</html>
```